Webdesign für Vernetzung christlicher Geschäftsleute
Zielgruppe
Die Vereinigung KRTWLE bezweckt die Vernetzung christlicher Geschäftsleute und die Verbreitung von Biblisch fundierten ethischen Geschäftsprinzipien. Die Zielgruppe umfasst Unternehmer und Verantwortungsträger aus Wirtschaft und Politik.
Aufgabenstellung
Ich suche einen Designer, welcher sich ernsthaft mit den Anforderungen und dem Design auseinandersetzt und eine Individuelle Lösung gestaltet.
Das Logo sowie ein unverbindlicher Vorschlag für die Strukturierung liegen bei.
Bitte keine 08/15 Business Stock Fotos (Händeschütteln, Meetings, Präsentationen).
Das Design soll folgende Seiten beinhalten (Beschreibung folgt):
- Startseite
- Standardseite (Titel, Text mit Bildern)
- Event-Detail Seite (Titel, Ort, Datum, ev. Foto, Beschreibungstext, ev. Map)
- Chapter Startseite
Die bestehende Webseite ist kein Massstab ;).

```html
<!DOCTYPE html>
<html lang="de">
<head>
<meta charset="utf-8">
<title>KRTWLE – Event</title>
<link href="https://fonts.googleapis.com/css2?family=Catamaran:wght@400;500;600;700&family=Source+Sans+3:wght@400;600;700&display=swap" rel="stylesheet">
<style>
:root{
  --red:#ab1b22;
  --ink:#141414;
  --text:#3a3a3a;
  --page:#efefef;
  --band:#d4d4d4;
  --footer:#d9d9d9;
  --white:#ffffff;
  --map:#f3f3f3;
}
*{margin:0;padding:0;box-sizing:border-box}
html,body{width:806px;height:1200px;overflow:hidden}
body{position:relative;background:var(--page);font-family:"Catamaran",sans-serif;color:var(--ink)}
.header{position:absolute;left:0;top:0;width:806px;height:94px;background:var(--white)}
.brand{position:absolute;left:101px;top:34px;display:flex;align-items:center;gap:6px;font-family:"Catamaran",sans-serif;font-weight:700;font-size:20px;letter-spacing:1px;color:var(--ink)}
.brand-dot{width:12px;height:12px;border-radius:50%;background:var(--red)}
.lang{position:absolute;right:107px;top:15px;display:flex;font-family:"Source Sans 3",sans-serif;font-size:7px;font-weight:600;letter-spacing:.5px}
.lang span{padding:0 7px;border-left:1px solid #ddd;line-height:9px}
.lang span:first-child{border:0}
.lang span:last-child{padding-right:0}
.lang .active{color:var(--red)}
.nav{position:absolute;right:107px;top:63px;display:flex;gap:34px;font-weight:600;font-size:9px;letter-spacing:.5px}
.hero{position:absolute;left:0;top:94px;width:806px;height:243px;background:linear-gradient(135deg,#7a5c4a,#b0918a 35%,#5b6e8c 65%,#8d7564)}
.subnav{position:absolute;left:0;top:337px;width:806px;height:30px;background:var(--band);font-family:"Source Sans 3",sans-serif;font-size:7.2px}
.back{position:absolute;left:107px;top:10px;display:flex;align-items:center;gap:6px;font-weight:700}
.chapters{position:absolute;right:107px;top:11px;display:flex}
.chapters span{padding:0 7px;border-left:1px solid #555;line-height:8px}
.chapters span:first-child{border:0}
.chapters span:last-child{padding-right:0}
.event-photo{position:absolute;left:107px;top:470px;width:252px;height:249px;background:var(--white);box-shadow:0 10px 40px rgba(0,0,0,.08)}
.date-tag{position:absolute;left:90px;top:453px;width:36px;height:40px;background:var(--white);text-align:center;padding-top:6px}
.date-tag .month{font-size:8.5px;font-weight:500;line-height:9px}
.date-tag .day{font-size:15px;font-weight:700;line-height:16px}
.event{position:absolute;left:409px;top:478px;width:265px}
.event h1{font-size:16.5px;font-weight:600;line-height:19.5px}
.meta{margin-top:18px;font-size:8.2px;display:flex}
.meta span{padding:0 7px;border-left:1px solid #bbb;line-height:9px}
.meta span:first-child{padding-left:0;border:0}
.event p{margin-top:12px;font-size:8.2px;line-height:12.6px;color:var(--text)}
.event p.lead{color:var(--ink)}
.section-title{position:absolute;left:107px;top:822px;font-size:16.5px;font-weight:600}
.map{position:absolute;left:107px;top:854px;width:593px;height:218px;background:linear-gradient(120deg,#f6f6f6,#ececec 55%,#f4f4f4)}
.map-marker{position:absolute;left:260px;top:942px;font-weight:700;font-size:11px;letter-spacing:1px}
.contact-card{position:absolute;left:558px;top:828px;width:117px;height:151px;background:var(--red);color:var(--white);font-family:"Source Sans 3",sans-serif;font-size:7.2px;padding:22px 0 0 16px;box-shadow:0 8px 25px rgba(0,0,0,.15)}
.contact-card h2{font-size:7.4px;font-weight:700;margin-bottom:11px}
.row{display:flex;gap:7px;line-height:11px}
.row svg{flex:none;margin-top:2px}
.gap{height:20px}
.footer{position:absolute;left:0;top:1156px;width:806px;height:44px;background:var(--footer);font-family:"Source Sans 3",sans-serif;font-size:6.5px}
.copyright{position:absolute;left:107px;top:17px}
.legal{position:absolute;right:107px;top:17px;display:flex}
.legal span{padding:0 6px;border-left:1px solid #333;line-height:7px}
.legal span:first-child{border:0}
.legal span:last-child{padding-right:0}
</style>
</head>
<body>
<header class="header">
  <div class="brand"><span class="brand-dot"></span>KRTWLE</div>
  <div class="lang"><span class="active">DE</span><span>FR</span><span>IT</span></div>
  <nav class="nav"><span>Startseite</span><span>Über uns</span><span>Chapter</span><span>Kontakt</span></nav>
</header>

<div class="hero" role="img" aria-label="Foto: Geschäftsleute im Gespräch bei einem Stehempfang, von oben fotografiert"></div>

<div class="subnav">
  <div class="back">
    <svg width="10" height="10" viewBox="0 0 10 10"><circle cx="5" cy="5" r="4.4" fill="none" stroke="#111" stroke-width=".8"/><path d="M7 5H3M4.7 3.3 3 5l1.7 1.7" fill="none" stroke="#111" stroke-width=".8"/></svg>
    Chapters
  </div>
  <div class="chapters"><span>Chapter Seite 1</span><span>Chapter Seite 2</span><span>Chapter Seite 3</span><span>Chapter Seite 4</span><span>Chapter Seite 5</span></div>
</div>

<div class="event-photo" role="img" aria-label="Platz für ein Eventfoto"></div>
<div class="date-tag"><div class="month">AUG</div><div class="day">25</div></div>

<article class="event">
  <h1>Lorem ipsum dolor sit<br>amet consetetur</h1>
  <div class="meta"><span><b>Datum:</b> 25.08.2019</span><span><b>Uhrzeit:</b> 09:30 Uhr</span><span><b>Ort:</b> Auberge des Érables</span></div>
  <p class="lead">Stet clita kasd gubergren, no sea takimata sanctus est Lorem ipsum dolor sit amet. Lorem ipsum dolor sit amet, consetetur sadipscing elitr, sed diam nonumy eirmod tempor invidunt ut labo. <span style="color:var(--text)">Lorem ipsum dolor sit amet, consetetur sadipscing elitr, sed diam nonumy eirmod tempor invidunt ut labore et dolore magna aliquyam erat, sed diam voluptua.</span></p>
  <p>At vero eos et accusam et justo duo dolores et ea rebum. Stet clita kasd gubergren, no sea takimata sanctus est Lorem ipsum dolor sit amet. Lorem ipsum dolor sit amet, consetetur sadipscing elitr, sed diam nonumy eirmod tempor invidunt ut labore.</p>
</article>

<h2 class="section-title">Anfahrt</h2>
<div class="map" role="img" aria-label="Karte mit der Anfahrt zum Veranstaltungsort"></div>
<div class="map-marker">KRTWLE</div>

<aside class="contact-card">
  <h2>Eventname / Titel</h2>
  <div class="row"><svg width="8" height="9" viewBox="0 0 8 10"><path d="M4 0a3.5 3.5 0 0 0-3.5 3.5C.5 6 4 10 4 10s3.5-4 3.5-6.5A3.5 3.5 0 0 0 4 0Z" fill="#fff"/><circle cx="4" cy="3.5" r="1.3" fill="#ab1b22"/></svg><div>Musterstrasse 123<br>12345 Musterstadt</div></div>
  <div class="gap"></div>
  <div class="row"><svg width="8" height="8" viewBox="0 0 10 10"><path d="M2 0.5 4 3 3 4.2c.6 1.3 1.5 2.2 2.8 2.8L7 6l2.5 2-1 1.5C4.5 9.5.5 5.5.5 1.5Z" fill="#fff"/></svg><div>0123 / 456 789 - 0</div></div>
  <div class="row"><svg width="8" height="8" viewBox="0 0 10 10"><rect x=".5" y="2" width="9" height="6.5" fill="#fff"/><path d="M.5 2 5 5.5 9.5 2" fill="none" stroke="#ab1b22" stroke-width=".8"/></svg><div>info@krtwle.ch</div></div>
  <div class="row"><svg width="8" height="8" viewBox="0 0 10 10"><path d="M9.5.5 .5 4.5 5 5l.5 4.5Z" fill="#fff"/></svg><div>www.krtwle.ch</div></div>
</aside>

<footer class="footer">
  <div class="copyright">Copyright © 2019 Alle Rechte vorbehalten. Kreis Reformierter Tätiger Wirtschaftsleute</div>
  <div class="legal"><span>Kontakt</span><span>Datenschutz</span><span>Impressum</span></div>
</footer>
</body>
</html>
```